Stationery Design Project - Tax Professionals/Chartered Accountants

The name of our firm is “Penwick Group” and our slogan is “Bright Pathways”. You can also use the name "The Penwick Group" if it works better.

We are looking for a full stationery design: Letterhead, Business Card and With Compliments slip

We are looking for a bold, modern and clean/simple design that makes us stand out. We stand out as professionals in the industry and would like the stationery that our clients see to convey this image as well.

There is no colour preference.

We have used a "Lion" as our logo/symbol and that has received positive feedback from our clients; if you think the lion works then please incorporate the "lion".

If you think another symbol works then please submit this we are very open to ideas and would like to see designs that don't incorporate a lion as well.

We would like a corporate feel to this.

You could also incorporate the LG logo http://www.ledgerguildexample.com.au/Members/Marketing-your-practice/Logos but this is not a must.

WHO WE ARE:-
We are a Chartered Accounting firm who specialise in the delivery of taxation and strategic insolvency services. We also provide financial reporting services that help clients negotiate and compromise their debt or expenses such as rent with their landlords.

We work with Law Firms, other Accountants to deliver the best service for our clients.

Our clients come from varied backgrounds and are largely successful and established businesses and high net worth individuals looks for effective tax planning.

We are not the usual accounting firm and do not provide traditional tax return based services.
Updates

Reason: There are still designers who have signed on but not yet submitted designs and also adjustments to existing designs submitted. Extra time so designers are not rushed.

Target Market(s)

Corporate/ Independent successful businesses and individuals

Industry/Entity Type

Business

Requirements
Must have
• The letter must have the following phrase
“Liability limited by a scheme approved under Professional Standards Legislation”

The letter must also have the following business information:-
“The Penwick Group Pty Ltd atf
Principal - Colin T. Penwick
ABN: 47 215 708 362”

Plus Usual Address & Contact Details

We would also a logo or symbol that is representative of us. We like the idea of a lion but this is not set in stone and are very open to ideas.

```html
<!DOCTYPE html>
<html lang="en">
<head>
<meta charset="utf-8">
<title>Penwick Group – Stationery Suite</title>
<link rel="stylesheet" href="https://fonts.googleapis.com/css2?family=Roboto+Condensed:wght@400;700&display=swap">
<style>
  :root {
    --backdrop: #dcd8d0;
    --paper: #eeeeee;
    --paper-edge: #d6d6d6;
    --band: #9b9b9b;
    --panel: #8f8f8f;
    --logo: #a4a4a4;
    --ink: #9c9c9c;
    --ink-strong: #8a8a8a;
    --rule: #d2d2d2;
    --on-band: #ffffff;
    --text-font: "Roboto Condensed", "Arial Narrow", sans-serif;
  }
  * { box-sizing: border-box; margin: 0; padding: 0; }
  html, body { width: 1200px; height: 846px; overflow: hidden; }
  body { background: var(--backdrop); font-family: var(--text-font); }

  .canvas { position: relative; width: 1200px; height: 846px; }

  .sheet {
    position: absolute;
    background: var(--paper);
    border: 1px solid var(--paper-edge);
    overflow: hidden;
  }
  .band {
    position: absolute; left: 0; right: 0; bottom: 0;
    background: var(--band);
    color: var(--on-band);
    display: flex; align-items: center;
  }

  /* Wordmark: one font, one weight, one colour, plus a plain square */
  .wordmark {
    position: absolute;
    display: flex; flex-direction: column; align-items: center;
    color: var(--logo);
    font-family: var(--text-font);
    font-weight: 700;
    text-transform: uppercase;
    line-height: 1;
  }
  .wordmark .mark-square {
    background: var(--logo);
    margin-bottom: 0.3em;
  }
  .wordmark .name-main { white-space: nowrap; letter-spacing: 0.02em; }
  .wordmark .name-sub {
    white-space: nowrap;
    font-size: 0.6em;
    letter-spacing: 0.7em;
    margin-right: -0.7em;
    margin-top: 0.1em;
  }

  .details { position: absolute; color: var(--ink); line-height: 1.4; }
  .details strong { color: var(--ink-strong); font-weight: 700; }
  .details .group { padding: 6px 0; border-bottom: 1px solid var(--rule); }
  .details .group + .group { padding-top: 7px; }

  /* Business card – landscape */
  .card-landscape { left: 60px; top: 96px; width: 243px; height: 141px; }
  .card-landscape .side-panel {
    position: absolute; left: 0; top: 0; bottom: 0; width: 106px;
    background: var(--panel); color: var(--on-band);
  }
  .card-landscape .holder { position: absolute; left: 11px; top: 24px; font-size: 10px; font-weight: 700; line-height: 1.3; }
  .card-landscape .address { position: absolute; left: 11px; top: 94px; font-size: 7.5px; line-height: 1.45; }
  .card-landscape .wordmark { left: 114px; width: 120px; top: 22px; font-size: 22px; }
  .card-landscape .wordmark .mark-square { width: 26px; height: 26px; }
  .card-landscape .phones { position: absolute; left: 120px; top: 117px; font-size: 7.5px; color: var(--ink-strong); white-space: nowrap; }

  /* Business card – portrait */
  .card-portrait { left: 342px; top: 44px; width: 140px; height: 242px; }
  .card-portrait .wordmark { left: 0; right: 0; top: 26px; font-size: 24px; }
  .card-portrait .wordmark .mark-square { width: 30px; height: 30px; }
  .card-portrait .holder { position: absolute; left: 0; right: 0; top: 134px; text-align: center; font-size: 10px; font-weight: 700; color: var(--ink-strong); line-height: 1.35; }
  .card-portrait .address { position: absolute; left: 0; right: 0; top: 172px; text-align: center; font-size: 7.5px; color: var(--ink); line-height: 1.5; }
  .card-portrait .band { height: 25px; justify-content: center; font-size: 7.5px; font-weight: 700; }

  /* Letterhead */
  .letterhead { left: 556px; top: 42px; width: 580px; height: 750px; }
  .letterhead .details { left: 25px; top: 24px; width: 92px; font-size: 7.5px; }
  .letterhead .wordmark { left: 170px; width: 220px; top: 26px; font-size: 42px; }
  .letterhead .wordmark .mark-square { width: 56px; height: 56px; }
  .letterhead .band { height: 28px; justify-content: flex-end; padding-right: 128px; font-size: 7.5px; letter-spacing: 0.03em; }

  /* DL envelope */
  .envelope { left: 75px; top: 335px; width: 660px; height: 290px; }
  .envelope .wordmark { left: 20px; width: 130px; top: 28px; font-size: 24px; }
  .envelope .wordmark .mark-square { width: 38px; height: 38px; }
  .envelope .details { left: 20px; top: 140px; width: 130px; font-size: 10px; }
  .envelope .details .group { border-top: 1px solid var(--rule); padding: 8px 6px; }
  .envelope .band { height: 29px; }

  /* With compliments slip */
  .comp-slip { left: 247px; top: 454px; width: 538px; height: 256px; }
  .comp-slip .details { left: 30px; top: 40px; width: 96px; font-size: 7.5px; }
  .comp-slip .wordmark { left: 320px; width: 200px; top: 40px; font-size: 40px; }
  .comp-slip .wordmark .mark-square { width: 62px; height: 62px; }
  .comp-slip .band { height: 39px; justify-content: flex-end; padding-right: 18px; font-size: 16px; letter-spacing: 0.08em; }
</style>
</head>
<body>
<main class="canvas">

  <section class="sheet letterhead" aria-label="Letterhead">
    <div class="details">
      <div class="group">
        The Penwick Group Pty Ltd atf<br>
        <strong>Principal - Colin T. Penwick</strong><br>
        ABN: 47 215 708 362
      </div>
      <div class="group">
        Suite 3, L3 Marlow House<br>
        14 Kestrel Ave., Seacliff<br>
        QLD 4299 PO Box 2087
      </div>
    </div>
    <div class="wordmark"><span class="mark-square"></span><span class="name-main">Penwick</span><span class="name-sub">Group</span></div>
    <div class="band">Liability limited by a scheme approved under Professional Standards Legislation</div>
  </section>

  <section class="sheet card-landscape" aria-label="Business card, landscape">
    <div class="side-panel">
      <p class="holder">Colin T. Penwick<br>Principal</p>
      <p class="address">Suite 3, L3 Marlow House<br>14 Kestrel Ave., Seacliff<br>QLD 4299&nbsp; PO Box 2087</p>
    </div>
    <div class="wordmark"><span class="mark-square"></span><span class="name-main">Penwick</span><span class="name-sub">Group</span></div>
    <p class="phones">T 07 5000 4182&nbsp;&nbsp; F 07 5000 4190</p>
  </section>

  <section class="sheet card-portrait" aria-label="Business card, portrait">
    <div class="wordmark"><span class="mark-square"></span><span class="name-main">Penwick</span><span class="name-sub">Group</span></div>
    <p class="holder">Colin T. Penwick<br>Principal</p>
    <p class="address">Suite 3, L3 Marlow House<br>14 Kestrel Ave., Seacliff<br>QLD 4299&nbsp; PO Box 2087</p>
    <div class="band">T 07 5000 4182&nbsp;&nbsp; F 07 5000 4190</div>
  </section>

  <section class="sheet envelope" aria-label="DL envelope">
    <div class="wordmark"><span class="mark-square"></span><span class="name-main">Penwick</span><span class="name-sub">Group</span></div>
    <div class="details">
      <div class="group">
        Suite 3, L3 Marlow House<br>
        14 Kestrel Ave., Seacliff<br>
        QLD 4299&nbsp; PO Box 2087
      </div>
    </div>
    <div class="band"></div>
  </section>

  <section class="sheet comp-slip" aria-label="With compliments slip">
    <div class="details">
      <div class="group">
        The Penwick Group Pty Ltd atf<br>
        <strong>Principal - Colin T. Penwick</strong><br>
        ABN: 47 215 708 362
      </div>
      <div class="group">
        Suite 3, L3 Marlow House<br>
        14 Kestrel Ave., Seacliff<br>
        QLD 4299 PO Box 2087
      </div>
    </div>
    <div class="wordmark"><span class="mark-square"></span><span class="name-main">Penwick</span><span class="name-sub">Group</span></div>
    <div class="band">WITH COMPLIMENTS</div>
  </section>

</main>
</body>
</html>
```